依頼詳細
依頼の詳細や参考URL等は添付の「依頼詳細.txt」に全てまとめましたので、そちらをご確認ください。
トップページのラフイメージは「toppage_image.jpg」を参照下さい。
サイトURL
ページ数
1ページ
希望イメージ
シンプル 複雑
単色 カラフル
暗い 明るい
日常 高級
遊び心 厳粛
未来的 伝統的
女性的 男性的
希望する色
背景色:アイボリー。差し色:薄紫色など淡い色で何色か使用。
納品ファイル
• イラストレーター形式 (.ai)
• フォトショップ形式 (.psd)
補足説明

レベルがみなさん高かったので非常に迷いましたが、水彩がうまくマッチしていて、ごあいさつや保育目標などの部分のデザインも気に入りましたのでこちらにしました。

今回はコンペに参加していただき、誠にありがとうございました。
みなさん素晴らしいデザインで迷いましたが、またコンペを依頼する際にはご提案していただけたら幸いです。

```html
<!DOCTYPE html>
<html lang="ja">
<head>
<meta charset="utf-8">
<title>ひかりほいくえん</title>
<link href="https://fonts.googleapis.com/css2?family=M+PLUS+Rounded+1c:wght@400;700;800&display=swap" rel="stylesheet">
<style>
:root{
  --ivory:#f7f2e2;
  --cream:#fffbef;
  --brown:#5a3a22;
  --text:#4a3a2e;
  --red:#e2352e;
  --pink:#f49bb0;
  --blue:#a9d6f2;
  --lime:#d6ea8a;
  --lavender:#c9a9e6;
  --orange:#f8b25a;
  --rose:#f6a6c8;
  --green:#c7e897;
  --tag:#7a4e2c;
}
*{box-sizing:border-box;margin:0;padding:0}
html,body{width:1200px;height:4184px;overflow:hidden}
body{background:var(--ivory);font-family:"M PLUS Rounded 1c",sans-serif;color:var(--text);position:relative}
.header{height:160px;position:relative;background:var(--cream)}
.tagline{position:absolute;left:32px;top:14px;font-size:18px;color:#9a7a58}
.brand{position:absolute;left:32px;top:40px;display:flex;align-items:center;gap:16px;font-size:58px;font-weight:800;color:var(--brown)}
.brand i{width:52px;height:52px;border-radius:50%;background:#f2a33a;display:block}
.contact{position:absolute;right:40px;top:24px;text-align:right}
.contact .en{font-size:30px;font-weight:800;color:var(--brown);display:flex;align-items:center;gap:10px;justify-content:flex-end}
.contact .en i{width:28px;height:28px;background:#8cc63f;display:block;border-radius:6px}
.contact .tel{margin-top:10px;display:inline-flex;align-items:center;gap:10px;background:#f39ab0;color:#fff;font-size:34px;font-weight:700;padding:4px 18px;border-radius:10px}
.nav{display:flex;height:48px;padding:0 8px;gap:6px;background:var(--cream)}
.nav a{flex:1;display:flex;align-items:center;justify-content:center;font-size:18px;font-weight:700;color:#fff;text-decoration:none;border-radius:10px 10px 0 0}
.nav a:nth-child(1){background:var(--red)}
.nav a:nth-child(2){background:#f39a3a}
.nav a:nth-child(3){background:#e8c43a}
.nav a:nth-child(4){background:#8cc63f}
.nav a:nth-child(5){background:#4fb3e0}
.nav a:nth-child(6){background:#a27ad4}
.nav a:nth-child(7){background:#e47fb0}
.hero{height:520px;background:linear-gradient(90deg,#d9b98a 0%,#c9a26d 18%,#9fb7cf 35%,#c7d8e8 55%,#b9c99a 80%,#e8c27a 100%)}
.dots{display:flex;gap:18px;justify-content:center;margin-top:14px}
.dots span{width:16px;height:16px;border-radius:50%;background:#cbbfa8}
.dots span:nth-child(2){background:#7a5a3a}
.tag{display:inline-block;background:var(--tag);color:#fff;font-size:30px;font-weight:800;line-height:1.3;padding:8px 28px;border-radius:8px 30px 30px 8px;position:absolute;z-index:5}
.notice{position:absolute;left:140px;top:840px;width:920px;height:520px;background:var(--red);border-radius:40px}
.notice .board{position:absolute;left:60px;top:50px;right:60px;bottom:130px;background:#fff6c9;border-radius:60px}
.notice .train{position:absolute;left:240px;right:120px;bottom:24px;height:200px;border-radius:30px;background:linear-gradient(90deg,#f0c04a,#7fc3e6,#f39ab0,#a5d46a)}
.greeting{position:absolute;left:160px;top:1500px;width:880px;font-size:22px;line-height:1.75}
.goals{position:absolute;left:0;top:1920px;width:1200px;height:240px;background:repeating-linear-gradient(180deg,#fde0c8 0 20px,#fff3e6 20px 40px);display:flex;justify-content:center;gap:50px;align-items:center}
.goal{width:222px;height:222px;border-radius:50%;color:#fff;text-align:center;font-size:17px;font-weight:700;line-height:1.45;padding-top:30px;border:6px solid #fff;flex:none}
.goal b{display:block;margin:0 auto 10px;width:44px;height:44px;border-radius:50%;border:3px solid #fff;font-size:26px;line-height:38px}
.goal:nth-child(1){background:#6fb8e6}
.goal:nth-child(2){background:#f39ab0}
.goal:nth-child(3){background:#8cc63f}
.goal:nth-child(4){background:#a27ad4}
.features{position:absolute;left:160px;top:2260px;width:888px;display:grid;grid-template-columns:428px 428px;gap:40px 32px}
.card{height:280px;border-radius:24px;padding:22px;position:relative}
.card .num{display:inline-block;width:40px;height:40px;border-radius:50%;background:#fff;text-align:center;line-height:40px;font-weight:800;font-size:22px;color:var(--brown)}
.card h3{font-size:44px;font-weight:800;color:#fff;margin-top:4px}
.card .photo{position:absolute;right:22px;top:22px;width:190px;height:140px;border-radius:10px}
.card p{position:absolute;left:22px;right:22px;top:170px;font-size:17px;line-height:1.6}
.c1{background:var(--pink)}.c2{background:var(--blue)}.c3{background:var(--lime)}
.c4{background:var(--lavender)}.c5{background:var(--orange)}.c6{background:var(--rose)}
.c1 .photo{background:linear-gradient(135deg,#b98a5a,#e6c79a)}
.c2 .photo{background:linear-gradient(135deg,#f1eadc,#cfc4b0)}
.c3 .photo{background:linear-gradient(135deg,#e0b07a,#9cc3e0)}
.c4 .photo{background:linear-gradient(135deg,#b2742e,#e3b36f)}
.c5 .photo{background:linear-gradient(135deg,#d5c1a1,#8fa9c8)}
.c6 .photo{background:linear-gradient(135deg,#c9d6e3,#e2c49a)}
.access{position:absolute;left:160px;top:3320px;width:880px;height:320px;background:#fff;border-radius:16px;padding:12px}
.access .map{position:absolute;left:12px;top:12px;width:420px;height:296px;background:linear-gradient(135deg,#eeeae2,#dcd8cf)}
.access .building{position:absolute;left:448px;top:12px;width:420px;height:190px;background:linear-gradient(135deg,#c7d6e6,#d9b98a)}
.access address{position:absolute;left:448px;top:218px;font-style:normal;font-size:18px;line-height:1.6}
.footer{position:absolute;left:0;top:3700px;width:1200px;height:420px;background:var(--green)}
.footer ul{list-style:none;position:absolute;top:50px;font-size:19px;line-height:2.2}
.footer li::before{content:"";display:inline-block;width:8px;height:8px;border-radius:50%;background:#6a9a3a;margin-right:10px;vertical-align:middle}
.footer .bird{position:absolute;right:70px;top:80px;width:170px;height:300px;border-radius:40px;background:linear-gradient(180deg,#c6e2f0,#f3d58a)}
.copy{position:absolute;left:0;top:4140px;width:1200px;height:44px;background:var(--brown);color:#fff;text-align:center;font-size:16px;line-height:44px}
</style>
</head>
<body>
<header class="header">
  <div class="tagline">みどり市にある私立保育園</div>
  <div class="brand"><i></i>ひかりほいくえん</div>
  <div class="contact">
    <div class="en"><i></i>Hikari nursery</div>
    <div class="tel">
      <svg width="28" height="28" viewBox="0 0 24 24"><path fill="#fff" d="M6.6 10.8a15 15 0 006.6 6.6l2.2-2.2a1 1 0 011-.25 11.4 11.4 0 003.6.6 1 1 0 011 1V20a1 1 0 01-1 1A17 17 0 013 4a1 1 0 011-1h3.5a1 1 0 011 1c0 1.25.2 2.45.6 3.6a1 1 0 01-.25 1z"/></svg>
      0500-12-3456
    </div>
  </div>
</header>
<nav class="nav">
  <a>トップページ</a><a>園の案内</a><a>保育の特色</a><a>保育園の一日</a><a>年間行事</a><a>お知らせ</a><a>保護者様用</a>
</nav>
<div class="hero" role="img" aria-label="園舎と園庭で遊ぶ子どもたちの写真"></div>
<div class="dots"><span></span><span></span><span></span></div>

<span class="tag" style="left:160px;top:790px">お知らせ</span>
<section class="notice">
  <div class="board"></div>
  <div class="train" role="img" aria-label="動物たちが乗った汽車のイラスト"></div>
</section>

<span class="tag" style="left:160px;top:1430px">ごあいさつ</span>
<section class="greeting">
  <p>3歳未満児については、家庭的な雰囲気の中で毎日を健やかに過ごすことが出来るように配慮するとともに愛情を注いでいきます。</p>
  <p>幼児については、自分が考えたり創ったりする遊びを体験したり、「縦割り」保育と「横割り」保育を組み合わせた保育環境の中で楽しく遊んでたくさん学び、思いやりの心やリーダーシップを育てます。</p>
  <p>また、小学校の連携がスムーズに行えるように、学ぶべき課題を段階をおって学んでいきます。</p>
</section>

<span class="tag" style="left:160px;top:1860px">保育目標</span>
<section class="goals">
  <div class="goal"><b>1</b>心身ともに<br>丈夫で<br>よく遊ぶこども</div>
  <div class="goal"><b>2</b>誰とでも仲良く<br>伸び伸びと元気に<br>遊ぶこども</div>
  <div class="goal"><b>3</b>生活のきまりを<br>守り規則正しく<br>生活できるこども</div>
  <div class="goal"><b>4</b>創意工夫し<br>最後まで<br>やり遂げる子ども</div>
</section>

<span class="tag" style="left:160px;top:2200px">園の特色</span>
<section class="features">
  <div class="card c1"><span class="num">1</span><h3>もじ</h3><div class="photo" role="img" aria-label="文字を学ぶ子どもたちの写真"></div><p>年中から文字書きの基礎練習を始めます。小学校の教科書を使って文章を読む力を育てます。</p></div>
  <div class="card c2"><span class="num">2</span><h3>かず</h3><div class="photo" role="img" aria-label="かずの練習ノートの写真"></div><p>1つの数を合わせたり、分けたりと、足し算、引き算の概念にも触れます。</p></div>
  <div class="card c3"><span class="num">3</span><h3>ちえ</h3><div class="photo" role="img" aria-label="知恵遊びをする子どもの写真"></div><p>知識を応用する思考・能力を身に付けます。</p></div>
  <div class="card c4"><span class="num">4</span><h3>おんがく</h3><div class="photo" role="img" aria-label="カスタネットの写真"></div><p>カスタネット、太鼓、ハンドベル、鍵盤ハーモニカなど、様々な楽器に触れ、音楽を感じる心を育てます。</p></div>
  <div class="card c5"><span class="num">5</span><h3>鼓隊</h3><div class="photo" role="img" aria-label="鼓隊の演奏の写真"></div><p>年長は鼓隊演奏に取り組みます。運動会で演奏を披露し、地域のパレードにも参加します。一人一人の自信につなげています。</p></div>
  <div class="card c6"><span class="num">6</span><h3>課外教室</h3><div class="photo" role="img" aria-label="課外教室の様子の写真"></div><p>通常保育終了後、外部講師による課外教室を開講しています。英語教室、体操教室などがあります。</p></div>
</section>

<span class="tag" style="left:160px;top:3250px">アクセス</span>
<section class="access">
  <div class="map" role="img" aria-label="園周辺の地図"></div>
  <div class="building" role="img" aria-label="園舎の外観写真"></div>
  <address>(社福)みどり会 ひかり保育園<br>〒000-0000 みどり市さくら町1丁目2-3<br>TEL/FAX 0500-12-3456</address>
</section>

<footer class="footer">
  <ul style="left:160px"><li>トップページ</li><li>園の案内</li><li>保育の特色</li></ul>
  <ul style="left:420px"><li>保育園の一日</li><li>年間行事</li><li>お知らせ</li></ul>
  <ul style="left:680px"><li>保護者様用</li><li>保護者様へ</li></ul>
  <div class="bird" role="img" aria-label="鳥のイラスト"></div>
</footer>
<div class="copy">copyright (c) Hikari nursery ,Inc.</div>
</body>
</html>
```